Business Card & Stationary
For Event Planning Website
I need single sided standard sized Business Card [3.5" x 2"]
Same as logo or similar
Professional
First Name Last Name
Founder & Chief Executive Officer
Address 1
Address 2
New York, NY 10016
xyz@juniperhours.com
www.juniperhours.com
Feel free to be creative - the site is for party planning (weddings, bar-mitzvahs, etc.) so it should be modern & professional, with a fun factor.
I used test data to protect personal data but I can supply you with all of the information you need later.
I'm not sure which eps file corresponds to the jpg.
This is the hamsa (hand) which is part of the logo
The hand - ai file
Webpage Background Pattern

```html
<!DOCTYPE html>
<html lang="en">
<head>
<meta charset="utf-8">
<title>juniperhours — Stationery Set</title>
<link href="https://fonts.googleapis.com/css2?family=Nunito+Sans:wght@400;600;700&display=swap" rel="stylesheet">
<style>
  :root {
    --brand-blue: #1f8ad2;
    --brand-blue-dark: #166fae;
    --pattern-blue: #b7dbf3;
    --paper: #ffffff;
    --ink: #4a4f55;
    --ink-soft: #8a9097;
    --backdrop: #1b1c1e;
  }
  * { box-sizing: border-box; margin: 0; padding: 0; }
  html, body {
    width: 1200px; height: 899px; overflow: hidden;
    background: var(--backdrop);
    font-family: "Nunito Sans", Arial, sans-serif;
    color: var(--ink);
  }
  .stationery-set { position: relative; width: 1200px; height: 899px; }

  .brand { display: flex; align-items: center; gap: 6px; color: var(--brand-blue); font-weight: 600; letter-spacing: -0.3px; }
  .brand-dot { width: 0.55em; height: 0.55em; border-radius: 50%; background: var(--brand-blue); }
  .brand--light { color: var(--paper); }
  .brand--light .brand-dot { background: var(--paper); }

  .motif {
    position: absolute; border-radius: 50%;
    background: radial-gradient(circle at 45% 45%, var(--pattern-blue) 0%, rgba(183,219,243,0.55) 55%, rgba(183,219,243,0) 72%);
  }

  /* Letterhead */
  .letterhead {
    position: absolute; left: 60px; top: 140px; width: 430px; height: 608px;
    background: var(--paper); overflow: hidden;
  }
  .letterhead .brand { position: absolute; left: 36px; top: 34px; font-size: 24px; }
  .letter-body { position: absolute; left: 36px; top: 100px; width: 300px; font-size: 9px; line-height: 1.55; }
  .letter-body p { margin-bottom: 9px; }
  .letter-date { color: var(--ink-soft); }
  .letter-sign strong { color: var(--brand-blue-dark); font-weight: 700; }
  .letterhead .motif { width: 230px; height: 230px; right: -30px; bottom: 20px; }
  .letter-footer {
    position: absolute; left: 0; bottom: 0; width: 100%; height: 26px;
    background: var(--brand-blue); color: var(--paper);
    font-size: 7.5px; display: flex; align-items: center; justify-content: center; gap: 8px;
  }

  /* Business cards */
  .card {
    position: absolute; width: 300px; height: 171px; border-radius: 10px; overflow: hidden;
  }
  .card--front { background: var(--brand-blue); color: var(--paper); }
  .card--back { background: var(--paper); display: flex; align-items: center; justify-content: center; }
  .card--front .brand { position: absolute; left: 20px; top: 22px; font-size: 20px; }
  .card-details { position: absolute; right: 20px; bottom: 18px; text-align: right; font-size: 8.5px; line-height: 1.5; }
  .card-name { font-size: 12px; font-weight: 700; }
  .card-title { margin-bottom: 6px; opacity: 0.9; }
  .card-stripe { position: absolute; left: 0; bottom: 0; width: 100%; height: 6px; background: var(--brand-blue-dark); }
  .card--back .brand { font-size: 22px; }
  .card--one { left: 540px; top: 60px; }
  .card--two { left: 540px; top: 250px; }
  .card--three { left: 860px; top: 60px; }
  .card--four { left: 860px; top: 250px; }

  /* Envelope */
  .envelope {
    position: absolute; left: 540px; top: 460px; width: 620px; height: 288px;
    background: var(--paper); overflow: hidden;
  }
  .envelope .brand { position: absolute; left: 34px; top: 34px; font-size: 28px; }
  .envelope-return { position: absolute; left: 36px; top: 78px; font-size: 9px; line-height: 1.5; color: var(--ink-soft); }
  .envelope .motif { width: 240px; height: 240px; right: -20px; top: -20px; }
  .envelope-band { position: absolute; left: 0; bottom: 0; width: 100%; height: 30px; background: var(--brand-blue); }
  .envelope-band-accent { position: absolute; left: 0; bottom: 30px; width: 100%; height: 4px; background: var(--brand-blue-dark); }
</style>
</head>
<body>
<main class="stationery-set">

  <section class="letterhead">
    <div class="brand"><span>juniperhours</span><span class="brand-dot"></span></div>
    <div class="letter-body">
      <p class="letter-date">March 12, 2024</p>
      <p>Ms. Lena Hart<br>240 Park Avenue South<br>New York, NY 10016</p>
      <p>Dear Lena,</p>
      <p>Thank you for choosing us to plan your celebration. We are delighted to help bring your vision to life, from the first idea to the final dance.</p>
      <p>Enclosed you will find a proposed timeline, a list of trusted vendors and a preliminary budget for your review.</p>
      <p>Please let us know if anything should be adjusted. We look forward to meeting with you next week.</p>
      <p class="letter-sign">Warm regards,<br><br><strong>Dana Tolbrek</strong><br>Founder &amp; Chief Executive Officer</p>
    </div>
    <div class="motif" role="img" aria-label="Faint decorative hand motif in light blue"></div>
    <footer class="letter-footer">
      <span>Address 1, Address 2, New York, NY 10016</span>
      <span>xyz@juniperhours.com</span>
      <span>www.juniperhours.com</span>
    </footer>
  </section>

  <article class="card card--front card--one">
    <div class="brand brand--light"><span>juniperhours</span><span class="brand-dot"></span></div>
    <div class="card-details">
      <div class="card-name">Dana Tolbrek</div>
      <div class="card-title">Founder &amp; Chief Executive Officer</div>
      <div>Address 1<br>Address 2<br>New York, NY 10016</div>
      <div>xyz@juniperhours.com</div>
      <div>www.juniperhours.com</div>
    </div>
    <div class="card-stripe"></div>
  </article>

  <article class="card card--front card--two">
    <div class="brand brand--light"><span>juniperhours</span><span class="brand-dot"></span></div>
    <div class="card-details">
      <div class="card-name">Dana Tolbrek</div>
      <div class="card-title">Founder &amp; Chief Executive Officer</div>
      <div>Address 1<br>Address 2<br>New York, NY 10016</div>
      <div>xyz@juniperhours.com</div>
      <div>www.juniperhours.com</div>
    </div>
    <div class="card-stripe"></div>
  </article>

  <article class="card card--back card--three">
    <div class="brand"><span>juniperhours</span><span class="brand-dot"></span></div>
  </article>

  <article class="card card--back card--four">
    <div class="brand"><span>juniperhours</span><span class="brand-dot"></span></div>
  </article>

  <section class="envelope">
    <div class="brand"><span>juniperhours</span><span class="brand-dot"></span></div>
    <div class="envelope-return">Address 1<br>Address 2<br>New York, NY 10016</div>
    <div class="motif" role="img" aria-label="Faint decorative hand motif in light blue"></div>
    <div class="envelope-band-accent"></div>
    <div class="envelope-band"></div>
  </section>

</main>
</body>
</html>
```